Copperleaf Studio New Website

Custom Wood Cabinetry and Precisions Wood Cutting website. I have created a pdf document with all the specs for the project and attached it. I am just typing stuff in here so it stops telling me my description is too short. Their once was a man from Nantucket.. he used to pee in a bucket.. roses are red, cardinals are birds, i wish they didn't require 300 words.
Number of Pages Required
1 page

```html
<!DOCTYPE html>
<html lang="en">
<head>
<meta charset="utf-8">
<title>Copperleaf Studio</title>
<link href="https://fonts.googleapis.com/css2?family=Montserrat:wght@500;600;700;800&family=Fira+Sans:wght@400;500;600&display=swap" rel="stylesheet">
<style>
:root{
  --copper:#93592d;
  --copper-dark:#7a4822;
  --paper:#f8f5f2;
  --ink:#1d1d1d;
  --muted:#3a3a3a;
  --line:#d9d2cb;
  --white:#ffffff;
}
*{box-sizing:border-box;margin:0;padding:0}
html,body{width:1200px;height:3308px;overflow:hidden}
body{background:var(--paper);font-family:"Fira Sans",sans-serif;color:var(--ink);position:relative}
.abs{position:absolute}
.header{position:absolute;left:0;top:0;width:1200px;height:138px;background:var(--white)}
.brand{position:absolute;display:flex;align-items:center;gap:10px;font-family:"Fira Sans",sans-serif;font-weight:600;color:var(--copper-dark)}
.brand .dot{border-radius:50%;background:var(--copper);flex:none}
.header .brand{left:134px;top:40px;font-size:30px}
.header .brand .dot{width:34px;height:34px}
.info{position:absolute;top:34px;display:flex;align-items:center;gap:14px;font-family:"Montserrat",sans-serif}
.icon{width:27px;height:27px;border-radius:50%;background:var(--copper);display:flex;align-items:center;justify-content:center;flex:none}
.info small{display:block;font-size:12px;color:var(--ink);line-height:1.5}
.info .phone{font-size:18px;font-weight:500}
.cart{position:absolute;left:967px;top:36px;display:flex;align-items:center;gap:8px;font-size:12px;font-family:"Montserrat",sans-serif}
.cart .badge{position:absolute;left:81px;top:-4px;width:18px;height:18px;border-radius:50%;background:var(--copper);color:#fff;font-size:11px;display:flex;align-items:center;justify-content:center}
.nav{position:absolute;top:96px;font-family:"Montserrat",sans-serif;font-size:16px;font-weight:500;color:var(--ink)}
.nav.active{color:var(--copper);font-weight:700;border-bottom:2px solid var(--copper);padding-bottom:3px}
.hero{position:absolute;left:0;top:138px;width:1200px;height:607px;background:linear-gradient(120deg,#7a4a28 0%,#b27a45 30%,#c28c55 50%,#8a5a33 75%,#3a2b22 100%)}
.hero h1{position:absolute;left:0;width:1200px;top:177px;text-align:center;font-family:"Montserrat",sans-serif;font-weight:800;font-size:39px;color:#fff;letter-spacing:.5px}
.hero p{position:absolute;left:0;width:1200px;top:229px;text-align:center;font-family:"Montserrat",sans-serif;font-weight:700;font-size:18px;color:#fff}
.hero .btn{position:absolute;left:517px;top:281px;width:167px;height:53px;background:#fff;color:var(--copper);font-family:"Montserrat",sans-serif;font-weight:700;font-size:18px;display:flex;align-items:center;justify-content:center}
.dots{position:absolute;top:561px;left:560px;display:flex;gap:12px;align-items:center}
.dots span{width:6px;height:6px;border-radius:50%;background:#fff}
.dots span.on{width:10px;height:10px;background:#f0a030;border:2px solid #fff}
.section-title{position:absolute;left:0;width:1200px;text-align:center;font-family:"Montserrat",sans-serif;font-weight:700;font-size:22px}
.tab{position:absolute;top:867px;height:49px;border:1px solid var(--ink);display:flex;align-items:center;justify-content:center;font-size:16px;background:var(--white)}
.tab.on{background:var(--copper);border-color:var(--copper);color:#fff}
.photo{position:absolute}
.product{position:absolute;top:1284px;width:229px;text-align:center}
.product h3{font-weight:400;font-size:16px}
.product .price{font-size:17px;margin-top:8px}
.product .add{display:inline-block;margin-top:11px;width:97px;height:31px;border:2px solid var(--copper);color:var(--copper);font-size:12px;line-height:27px}
.arrow{position:absolute;top:1097px}
.welcome small{position:absolute;left:134px;top:1471px;font-size:19px}
.welcome h2{position:absolute;left:134px;top:1496px;font-family:"Montserrat",sans-serif;font-weight:700;font-size:24px;color:var(--copper)}
.welcome .rule{position:absolute;left:134px;top:1540px;width:255px;height:3px;background:var(--copper)}
.welcome p{position:absolute;left:134px;top:1571px;width:440px;font-size:16px;line-height:22.5px;color:var(--muted)}
.welcome .btn{position:absolute;left:136px;top:1790px;width:126px;height:39px;background:var(--copper);color:#fff;font-family:"Montserrat",sans-serif;font-weight:700;font-size:13px;display:flex;align-items:center;justify-content:center}
.faq{position:absolute;height:50px;width:460px;border:1px solid var(--copper);background:var(--white);display:flex;align-items:center;justify-content:space-between;padding:0 14px 0 16px;font-size:14px}
.chev{width:19px;height:19px;border-radius:50%;background:var(--copper);display:flex;align-items:center;justify-content:center}
.quote{position:absolute;left:0;top:2437px;width:1200px;height:526px;background:linear-gradient(100deg,#3a3f44 0%,#4a3526 30%,#3b2a20 60%,#2c2a2a 100%)}
.quote h2{position:absolute;left:0;width:1200px;top:53px;text-align:center;font-family:"Montserrat",sans-serif;font-weight:700;font-size:27px;color:#fff}
.quote .rule{position:absolute;left:561px;top:104px;width:79px;height:3px;background:#fff}
.field{position:absolute;background:#fff;font-size:15px;padding:18px 20px;color:var(--ink)}
.quote .btn{position:absolute;left:496px;top:415px;width:208px;height:58px;background:var(--copper);color:#fff;font-family:"Montserrat",sans-serif;font-weight:700;font-size:18px;display:flex;align-items:center;justify-content:center}
.footer .brand{left:134px;top:3072px;font-size:36px}
.footer .brand .dot{width:40px;height:40px}
.fhead{position:absolute;top:3014px;font-family:"Montserrat",sans-serif;font-weight:700;font-size:13px}
.flinks{position:absolute;left:502px;top:3052px;font-size:12.5px;line-height:20px}
.fitem{position:absolute;display:flex;gap:12px;font-size:12.5px;line-height:16px}
.fitem .icon{width:22px;height:22px;margin-top:3px}
.fdivider{position:absolute;left:134px;top:3231px;width:932px;height:1px;background:var(--line)}
.copy{position:absolute;left:0;width:1200px;top:3264px;text-align:center;font-size:12px}
</style>
</head>
<body>

<header class="header">
  <div class="brand"><span class="dot"></span>Copperleaf Studio</div>
  <div class="info" style="left:550px">
    <span class="icon"><svg width="11" height="14" viewBox="0 0 11 14"><path d="M5.5 0C2.5 0 0 2.4 0 5.4 0 9.2 5.5 14 5.5 14S11 9.2 11 5.4C11 2.4 8.5 0 5.5 0zm0 7.4a2 2 0 110-4 2 2 0 010 4z" fill="#fff"/></svg></span>
    <div><small>2210 Alder Road</small><small>Fontana, CA 92335</small></div>
  </div>
  <div class="info" style="left:768px">
    <span class="icon"><svg width="13" height="13" viewBox="0 0 24 24"><path d="M6.6 10.8a15 15 0 006.6 6.6l2.2-2.2c.3-.3.7-.4 1-.2 1.1.4 2.3.6 3.6.6.6 0 1 .4 1 1V20c0 .6-.4 1-1 1A17 17 0 013 4c0-.6.4-1 1-1h3.5c.6 0 1 .4 1 1 0 1.3.2 2.5.6 3.6.1.3 0 .7-.2 1l-2.3 2.2z" fill="#fff"/></svg></span>
    <div><small>CALL US</small><span class="phone">888.888.8888</span></div>
  </div>
  <div class="cart">My Cart
    <svg width="38" height="34" viewBox="0 0 38 34"><path d="M2 3h6l5 19h19l4-14H11" fill="none" stroke="#7d7d7d" stroke-width="3" stroke-linejoin="round"/><circle cx="15" cy="29" r="3" fill="#7d7d7d"/><circle cx="29" cy="29" r="3" fill="#7d7d7d"/></svg>
    <span class="badge">0</span>
  </div>
  <span class="nav active" style="left:553px">HOME</span>
  <span class="nav" style="left:653px">ABOUT</span>
  <span class="nav" style="left:764px">FAQS</span>
  <span class="nav" style="left:856px">CONTACT</span>
  <span class="nav" style="left:983px">SERVICES</span>
</header>

<section class="hero" role="img" aria-label="Photo of a kitchen fitted with knotty alder wood cabinets, seen through a brick archway">
  <h1>CUSTOM WOOD ART PROJECTS</h1>
  <p>LOREM IPSUM IS SIMPLY DUMMY TEXT OF THE PRINTING</p>
  <span class="btn">READ MORE</span>
  <div class="dots"><span></span><span></span><span class="on"></span><span></span><span></span></div>
</section>

<h2 class="section-title" style="top:798px">OUR SERVICES</h2>
<span class="tab" style="left:292px;width:171px">Newest Creations</span>
<span class="tab on" style="left:481px;width:170px">Custom Cabinetry</span>
<span class="tab" style="left:666px;width:244px">CNC Precision Wood Cutting</span>

<svg class="arrow" style="left:72px" width="20" height="28" viewBox="0 0 20 28"><path d="M15 3L5 14l10 11" fill="none" stroke="#222" stroke-width="3"/></svg>
<svg class="arrow" style="left:1101px" width="20" height="28" viewBox="0 0 20 28"><path d="M5 3l10 11L5 25" fill="none" stroke="#222" stroke-width="3"/></svg>

<div class="photo" style="left:132px;top:952px;width:229px;height:311px;background:linear-gradient(160deg,#eceff1,#c9cdd0 60%,#8e9194)" role="img" aria-label="White built-in mudroom cabinets with hooks and bench"></div>
<div class="photo" style="left:370px;top:952px;width:229px;height:311px;background:linear-gradient(160deg,#9c7550,#6b4a2f 50%,#c9c2b5)" role="img" aria-label="Rustic wood entry cabinets around a doorway with coat hooks"></div>
<div class="photo" style="left:605px;top:952px;width:229px;height:311px;background:linear-gradient(160deg,#d1a36c,#a9774a 50%,#5e4b3d)" role="img" aria-label="Tall wooden bookshelf wall with a rolling ladder"></div>
<div class="photo" style="left:840px;top:952px;width:228px;height:311px;background:linear-gradient(160deg,#6a4a2e,#4a321f 55%,#b9b2a6)" role="img" aria-label="Dark stained kitchen cabinets with granite countertop"></div>

<div class="product" style="left:132px"><h3>CABINET 1</h3><div class="price">$25.00</div><span class="add">ADD TO CART</span></div>
<div class="product" style="left:370px"><h3>CABINET 2</h3><div class="price">$25.00</div><span class="add">ADD TO CART</span></div>
<div class="product" style="left:605px"><h3>CABINET 3</h3><div class="price">$25.00</div><span class="add">ADD TO CART</span></div>
<div class="product" style="left:840px"><h3>CABINET 4</h3><div class="price">$25.00</div><span class="add">ADD TO CART</span></div>

<section class="welcome">
  <small>WELCOME TO</small>
  <h2>COPPERLEAF STUDIO</h2>
  <div class="rule"></div>
  <p>There are many variations of passages of Lorem Ipsum available, but the majority have suffered alteration in some form, by injected humour, or randomised words which don't look even slightly believable. If you are going to use a passage of Lorem Ipsum, you need to be sure there isn't anything embarrassing hidden in the middle of text. All the Lorem Ipsum generators on the Internet tend to repeat predefined</p>
  <span class="btn">READ MORE</span>
  <div class="photo" style="left:619px;top:1451px;width:447px;height:507px;background:linear-gradient(170deg,#e9ebe6,#aeb3a8 45%,#9a7a55 70%,#d8d3c9)" role="img" aria-label="Finished kitchen with wood cabinets, steel fridge and granite island"></div>
  <div class="photo" style="left:376px;top:1764px;width:308px;height:170px;background:linear-gradient(160deg,#d9d4cb,#8b6a4b 45%,#4d3524)" role="img" aria-label="Close-up of a carved copper farmhouse sink in a wood cabinet"></div>
</section>

<h2 class="section-title" style="top:2042px">FAQ</h2>
<div class="faq" style="left:132px;top:2111px">Lorem Ipsum is simply dummy text of the printing?<span class="chev"><svg width="9" height="6" viewBox="0 0 9 6"><path d="M1 1l3.5 3.5L8 1" fill="none" stroke="#fff" stroke-width="1.6"/></svg></span></div>
<div class="faq" style="left:608px;top:2111px">There are many variations of passages of Lorem Ipsum?<span class="chev"><svg width="9" height="6" viewBox="0 0 9 6"><path d="M1 1l3.5 3.5L8 1" fill="none" stroke="#fff" stroke-width="1.6"/></svg></span></div>
<div class="faq" style="left:132px;top:2179px">Sed ut perspiciatis unde omnis iste natus error sit voluptatem?<span class="chev"><svg width="9" height="6" viewBox="0 0 9 6"><path d="M1 1l3.5 3.5L8 1" fill="none" stroke="#fff" stroke-width="1.6"/></svg></span></div>
<div class="faq" style="left:608px;top:2179px">But I must explain to you how all this mistaken idea ?<span class="chev"><svg width="9" height="6" viewBox="0 0 9 6"><path d="M1 1l3.5 3.5L8 1" fill="none" stroke="#fff" stroke-width="1.6"/></svg></span></div>
<div class="faq" style="left:132px;top:2247px">At vero eos et accusamus et iusto odio dignissimos ?<span class="chev"><svg width="9" height="6" viewBox="0 0 9 6"><path d="M1 1l3.5 3.5L8 1" fill="none" stroke="#fff" stroke-width="1.6"/></svg></span></div>
<div class="faq" style="left:608px;top:2247px">On the other hand, we denounce with righteous indignation?<span class="chev"><svg width="9" height="6" viewBox="0 0 9 6"><path d="M1 1l3.5 3.5L8 1" fill="none" stroke="#fff" stroke-width="1.6"/></svg></span></div>
<div class="faq" style="left:132px;top:2315px">Lorem Ipsum is simply dummy text of the printing?<span class="chev"><svg width="9" height="6" viewBox="0 0 9 6"><path d="M1 1l3.5 3.5L8 1" fill="none" stroke="#fff" stroke-width="1.6"/></svg></span></div>
<div class="faq" style="left:608px;top:2315px">There are many variations of passages of Lorem Ipsum?<span class="chev"><svg width="9" height="6" viewBox="0 0 9 6"><path d="M1 1l3.5 3.5L8 1" fill="none" stroke="#fff" stroke-width="1.6"/></svg></span></div>

<section class="quote" role="img" aria-label="Darkened photo of a wood kitchen with a window and a refrigerator">
  <h2>REQUEST A QUOTE</h2>
  <div class="rule"></div>
  <div class="field" style="left:270px;top:148px;width:321px;height:51px">First Name</div>
  <div class="field" style="left:605px;top:148px;width:321px;height:51px">Last Name</div>
  <div class="field" style="left:270px;top:216px;width:321px;height:52px">Email</div>
  <div class="field" style="left:605px;top:216px;width:321px;height:52px">Phone</div>
  <div class="field" style="left:270px;top:284px;width:659px;height:102px">Message</div>
  <span class="btn">REQUEST A QUOTE</span>
</section>

<footer class="footer">
  <div class="brand"><span class="dot"></span>Copperleaf Studio</div>
  <span class="fhead" style="left:502px">MENU</span>
  <div class="flinks">HOME<br>ABOUT<br>FAQS<br>CONTACT<br>SERVICES</div>
  <span class="fhead" style="left:671px">CONTACT US</span>
  <div class="fitem" style="left:671px;top:3054px"><span class="icon"></span><div>2210 Alder Road<br>Fontana, CA 92335</div></div>
  <div class="fitem" style="left:671px;top:3104px"><span class="icon"></span><div>Call Us<br>888.888.88888</div></div>
  <div class="fitem" style="left:671px;top:3155px"><span class="icon"></span><div>E mail Us<br>info@CopperleafStudio.com</div></div>
  <span class="fhead" style="left:962px">FOLLOW US</span>
  <div class="fitem" style="left:962px;top:3054px"><span class="icon"></span><div>Like us on<br>GROVEBOOK</div></div>
  <div class="fitem" style="left:962px;top:3104px"><span class="icon"></span><div>Follow us on<br>CHIRPER</div></div>
  <div class="fitem" style="left:962px;top:3155px"><span class="icon"></span><div>Follow us on<br>WORKLINK</div></div>
  <div class="fdivider"></div>
  <p class="copy">Copyright © 2021 All Rights Reserved</p>
</footer>

</body>
</html>
```